VELTRIX GROUP
Project: VXG LOGO
VXG LOGO - Trade
VXG LOGO
Use same font as used in my logo
FAISAL NOORi
GENERAL MANAGER
RIYADH
info@veltrixgroup-example.com
VXGROUP VXGROUP
following changes on your design no #158 the logo upper and left side of the letter head company name bottom and left side of the letter haead The business cards are also in the above pattern. waiting for your immediate response. thanks.

```html
<!DOCTYPE html>
<html lang="en">
<head>
<meta charset="UTF-8">
<title>Veltrix Group – Business Card</title>
<link href="https://fonts.googleapis.com/css2?family=Open+Sans:wght@400;700&display=swap" rel="stylesheet">
<style>
  :root {
    --brand-blue: #1b5fa6;
    --icon-navy: #1f3a5c;
    --text-dark: #2b2b2b;
    --canvas-bg: #f2f2f2;
    --card-bg: #ffffff;
    --card-edge: #d6d6d6;
    --divider: #d9d9d9;
  }
  * { margin: 0; padding: 0; box-sizing: border-box; }
  html, body {
    width: 1200px; height: 871px; overflow: hidden;
    background: var(--canvas-bg);
    font-family: "Open Sans", Arial, sans-serif;
  }
  .business-card {
    position: absolute; left: 151px; top: 180px;
    width: 892px; height: 499px;
    background: var(--card-bg);
    border: 2px solid var(--card-edge);
  }
  .name-band {
    position: absolute; left: 0; top: 94px;
    width: 358px; height: 76px;
    background: var(--brand-blue);
    clip-path: polygon(0 0, 100% 0, 94% 100%, 0 100%);
    color: #fff;
    padding: 11px 0 0 51px;
  }
  .person-name { font-size: 28px; font-weight: 700; line-height: 1.1; letter-spacing: 0.3px; }
  .person-title { font-size: 13px; font-weight: 700; letter-spacing: 0.4px; margin-top: 2px; }
  .contact-list { position: absolute; left: 39px; top: 216px; list-style: none; }
  .contact-item {
    display: flex; align-items: center;
    height: 40px;
    font-size: 22px; color: var(--text-dark);
  }
  .contact-icon { width: 28px; height: 28px; margin-right: 14px; flex: none; }
  .divider {
    position: absolute; left: 447px; top: 58px;
    width: 2px; height: 386px;
    background: var(--divider);
  }
  .brand-lockup {
    position: absolute; left: 670px; top: 240px;
    transform: translate(-50%, -50%);
    display: flex; align-items: center; gap: 14px;
    color: var(--brand-blue); font-weight: 700;
    white-space: nowrap;
  }
  .brand-square { width: 30px; height: 30px; background: var(--brand-blue); flex: none; }
  .brand-name { font-size: 34px; line-height: 1; }
</style>
</head>
<body>
  <div class="business-card">
    <div class="name-band">
      <div class="person-name">FAISAL NOORi</div>
      <div class="person-title">GENERAL MANAGER</div>
    </div>

    <ul class="contact-list">
      <li class="contact-item">
        <svg class="contact-icon" viewBox="0 0 28 28"><circle cx="14" cy="14" r="12.5" fill="none" stroke="var(--icon-navy)" stroke-width="2"/><rect x="8" y="9.5" width="12" height="9" fill="var(--icon-navy)"/><path d="M8 10 L14 15 L20 10" fill="none" stroke="#fff" stroke-width="1.4"/></svg>
        info@veltrixgroup-example.com
      </li>
      <li class="contact-item">
        <svg class="contact-icon" viewBox="0 0 28 28"><circle cx="14" cy="14" r="12.5" fill="none" stroke="var(--icon-navy)" stroke-width="2"/><circle cx="14" cy="14" r="7" fill="none" stroke="var(--icon-navy)" stroke-width="1.6"/><ellipse cx="14" cy="14" rx="3" ry="7" fill="none" stroke="var(--icon-navy)" stroke-width="1.4"/><line x1="7" y1="14" x2="21" y2="14" stroke="var(--icon-navy)" stroke-width="1.4"/></svg>
        www@vxg-example.com
      </li>
      <li class="contact-item">
        <svg class="contact-icon" viewBox="0 0 28 28"><circle cx="14" cy="14" r="12.5" fill="none" stroke="var(--icon-navy)" stroke-width="2"/><path d="M14 21 C10 16 9 14 9 12 A5 5 0 0 1 19 12 C19 14 18 16 14 21 Z" fill="var(--icon-navy)"/><circle cx="14" cy="12" r="2" fill="#fff"/></svg>
        Riyadh, Saudi Arabia
      </li>
      <li class="contact-item">
        <svg class="contact-icon" viewBox="0 0 28 28"><circle cx="14" cy="14" r="12.5" fill="none" stroke="var(--icon-navy)" stroke-width="2"/><path d="M9.5 8 L12 8 L13 11 L11.5 12.5 C12.3 14.3 13.7 15.7 15.5 16.5 L17 15 L20 16 L20 18.5 C20 19.3 19.3 20 18.5 20 C13.3 19.5 8.5 14.7 8 9.5 C8 8.7 8.7 8 9.5 8 Z" fill="var(--icon-navy)"/></svg>
        +96610000555
      </li>
      <li class="contact-item">
        <svg class="contact-icon" viewBox="0 0 28 28"><circle cx="14" cy="14" r="12.5" fill="none" stroke="var(--icon-navy)" stroke-width="2"/><rect x="8" y="11" width="12" height="9" fill="var(--icon-navy)"/><rect x="10" y="7" width="8" height="4" fill="none" stroke="var(--icon-navy)" stroke-width="1.4"/><rect x="10" y="13" width="8" height="2" fill="#fff"/><rect x="10" y="16.5" width="3" height="2" fill="#fff"/><rect x="15" y="16.5" width="3" height="2" fill="#fff"/></svg>
        +96610000666
      </li>
    </ul>

    <div class="divider"></div>

    <div class="brand-lockup">
      <div class="brand-square"></div>
      <div class="brand-name">VELTRIX GROUP</div>
    </div>
  </div>
</body>
</html>
```